PLOVE clinical trial results Infographic

We need an infographic which presents the results from the PLOVE research trial. It should be colourful and engaging, in understandable language and showing the steps to get to the results. This is to showcase the results to patients/the public/clinicians, giving a brief summary of what the study proved. The final design should have the PLOVE logo at the top (please see attached and https://plove.brantu.fenmarsh.ac.uk/)
I have attached the required logos which need to be used (PLOVE, Brackwell Injury and Urgent Care, University of Fenmarsh) as well as an example from another study, PRUMEN3, as an example of what the layout could look like. Please DO NOT use the content from the PRUMEN3 example though, please instead use the content from the attached document 'PLOVE_InfographicDesignInformation_ArtHive'.

```html
<!DOCTYPE html>
<html lang="en">
<head>
<meta charset="utf-8">
<title>PLOVE trial results</title>
<link href="https://fonts.googleapis.com/css2?family=Outfit:wght@400;500;600;700&display=swap" rel="stylesheet">
<style>
:root{
  --navy:#0d1f5e;
  --coral:#e85d4f;
  --brick:#b6453f;
  --ink:#1c1c1c;
  --mist:#eff0f1;
  --line:#cfd2d6;
}
*{box-sizing:border-box;margin:0;padding:0}
html,body{width:936px;height:1200px;overflow:hidden;background:#fff}
body{font-family:"Outfit",sans-serif;color:var(--ink);position:relative}
.sheet{position:absolute;left:48px;top:49px;width:841px;height:1089px;background:#fff;border-radius:18px;box-shadow:0 2px 14px rgba(0,0,0,.12);overflow:hidden}
.abs{position:absolute}
.brand{left:33px;top:14px}
.brand-name{font-size:40px;font-weight:700;color:var(--navy);letter-spacing:.5px;line-height:1}
.brand-tag{font-size:7px;color:var(--navy);margin-top:2px}
.uni{right:38px;top:12px;display:flex;align-items:center;gap:6px;font-size:11px;font-weight:600;color:var(--navy);width:80px;line-height:1.15}
.uni .sq{width:12px;height:12px;background:var(--navy);flex:none}
.hero-band{left:0;top:176px;width:841px;height:117px;background:var(--coral)}
.hero-photo{left:0;top:94px;width:299px;height:199px;background:linear-gradient(120deg,#c79a80 0%,#d9b39c 40%,#4fa6de 75%,#e85d4f 100%);border-top-right-radius:40px}
.title{left:354px;top:107px;width:430px;font-size:20px;font-weight:700;line-height:1.25;color:#111}
.lede{left:354px;top:187px;width:412px;font-size:18px;line-height:1.3;color:#fff}
.lede b{color:var(--navy);font-weight:700}
.step{top:320px;width:247px;height:199px;border:1px solid var(--line);border-radius:3px;background:linear-gradient(135deg,#fff 0%,#f4f5f6 60%,#eceeef 100%)}
.step h3{position:absolute;left:21px;top:24px;font-size:19px;font-weight:700;color:var(--navy)}
.step p{position:absolute;font-size:16.5px;line-height:1.22}
.step .art{position:absolute;border-radius:8px;background:linear-gradient(160deg,#dfe4ec,#c9d3e2)}
.s1{left:38px}.s2{left:296px}.s3{left:555px}
.bars{position:absolute;left:23px;top:137px;width:210px;font-size:13px;font-weight:500}
.bar-row{display:flex;align-items:center;height:23px}
.bar-row span.lab{width:70px}
.bar{height:12px;margin-right:8px}
.bar-row em{font-style:normal;color:var(--navy);font-weight:500;font-size:13.5px}
.note{position:absolute;right:18px;bottom:5px;font-size:11px;color:#555}
.proved{left:38px;top:539px;width:765px;height:113px;border:1px solid var(--line);border-radius:3px;background:#fafafa}
.proved .icon{position:absolute;left:47px;top:21px;width:70px;height:70px;border-radius:50%;background:var(--navy)}
.proved h3{position:absolute;left:158px;top:11px;font-size:20px;font-weight:700;color:var(--navy)}
.proved p{position:absolute;left:158px;top:43px;width:565px;font-size:16.5px;line-height:1.22}
.inc-band{left:0;top:707px;width:841px;height:112px;background:var(--mist)}
.inc-tab{left:0;top:669px;width:336px;height:39px;background:var(--coral);color:#fff;font-size:20px;font-weight:700;padding:8px 0 0 122px;z-index:2}
.divider{width:1px;background:var(--line)}
.inc-art{border-radius:8px;background:linear-gradient(160deg,#d7dde6,#bfc9d8)}
.inc-text{font-size:16.5px;line-height:1.22}
.tl-band{left:0;top:841px;width:841px;height:54px;background:var(--mist)}
.tl-tab{left:0;top:849px;width:153px;height:39px;background:var(--coral);color:#fff;font-size:20px;font-weight:700;text-align:center;padding-top:6px}
.tl-head{font-size:16px;font-weight:700;color:var(--navy)}
.tl-sub{font-size:13.5px;margin-top:1px}
.fund{left:67px;top:912px;width:694px;height:79px;border:1px solid var(--line);border-radius:4px;background:#fff}
.fund .art{position:absolute;left:18px;top:8px;width:62px;height:62px;border-radius:8px;background:linear-gradient(160deg,#f3c6bf,#e85d4f 70%,#0d1f5e)}
.fund p{position:absolute;left:117px;top:8px;width:560px;font-size:17px;line-height:1.18}
.partner{font-size:11px;color:#555;display:flex;align-items:center;gap:6px}
.partner .dot{width:11px;height:11px;border-radius:50%;background:var(--coral)}
.funder{display:flex;align-items:center;gap:6px;color:var(--navy)}
.funder .mark{font-size:21px;font-weight:700;line-height:1}
.funder .rule{width:1px;height:18px;background:var(--coral)}
.funder .full{font-size:9.5px;font-weight:600;line-height:1.15}
.foot-strip{left:0;top:1056px;width:520px;height:33px;background:var(--mist);font-size:13.5px}
.contact{left:520px;top:1001px;width:321px;height:88px;background:var(--navy);color:#fff}
.contact .name{position:absolute;left:55px;top:14px;font-size:16px;font-weight:700}
.contact .aff{position:absolute;left:55px;top:35px;font-size:11px}
.contact .mail{position:absolute;left:55px;top:58px;font-size:13.5px}
</style>
</head>
<body>
<div class="sheet">
  <div class="abs brand">
    <div class="brand-name">PLOVE</div>
    <div class="brand-tag">Pressure Limb Outcomes &amp; Vacuum Evaluation</div>
  </div>
  <div class="abs uni"><span class="sq"></span>University of Fenmarsh</div>

  <div class="abs hero-band"></div>
  <div class="abs hero-photo" role="img" aria-label="Photo of a seated adult holding their lower leg, foot in a blue cast"></div>
  <h1 class="abs title">Do ‘vacuum’ dressings reduce infection after major trauma fracture surgery?</h1>
  <p class="abs lede">Adults with closed <b>lower-limb fractures</b> in the context of major trauma were randomised at 24 UK hospitals to <b>negative pressure ‘vacuum’ dressings or standard dressings</b></p>

  <section class="abs step s1">
    <h3>Step 1</h3>
    <p style="left:21px;top:81px;width:122px">1,548 adults at 24 UK trauma hospitals</p>
    <div class="art" style="left:145px;top:18px;width:92px;height:170px" role="img" aria-label="Illustration of a clinician helping a patient on crutches with a leg cast"></div>
  </section>
  <section class="abs step s2">
    <h3>Step 2</h3>
    <p style="left:23px;top:66px;width:105px">No reduction in deep infection</p>
    <div class="art" style="left:152px;top:12px;width:86px;height:110px" role="img" aria-label="Illustration of two clinicians with a patient in a wheelchair"></div>
    <div class="bars">
      <div class="bar-row"><span class="lab">Vacuum</span><span class="bar" style="width:72px;background:var(--coral)"></span><em>5.8%</em></div>
      <div class="bar-row"><span class="lab">Standard</span><span class="bar" style="width:80px;background:var(--brick)"></span><em>6.7%</em></div>
    </div>
    <span class="note">(At 30 days)</span>
  </section>
  <section class="abs step s3">
    <h3>Step 3</h3>
    <div class="art" style="left:156px;top:8px;width:82px;height:90px" role="img" aria-label="Illustration of a doctor with a clipboard beside an older patient with a walking cane"></div>
    <p style="left:25px;top:106px;width:190px">No difference at 6 months ininfection, disability, quality of life, scar healing, or pain.</p>
  </section>

  <section class="abs proved">
    <div class="icon">
      <svg width="70" height="70" viewBox="0 0 70 70" aria-hidden="true"><g fill="#fff"><rect x="16" y="24" width="8" height="16" rx="1"/><path d="M27 24h20a4 4 0 0 1 0 8h-2a3.5 3.5 0 0 1 0 7h-6l2 8a3 3 0 0 1-6 1l-4-9h-4z"/></g></svg>
    </div>
    <h3>Study proved</h3>
    <p>Negative pressure wound therapy (‘vacuum’ dressings) did not reduce the risk of deep infection, nor improve results for patients after major trauma lower-limb surgery compared to standard dressing.</p>
  </section>

  <div class="abs inc-band"></div>
  <div class="abs inc-tab">Who Was Included?</div>
  <div class="abs inc-art" style="left:45px;top:712px;width:70px;height:104px" role="img" aria-label="Illustration of a bearded man in a wheelchair with a leg cast"></div>
  <p class="abs inc-text" style="left:191px;top:743px;width:210px">Adults 16+, major trauma, lower-limb fracture needing surgery</p>
  <div class="abs divider" style="left:442px;top:707px;height:112px"></div>
  <div class="abs inc-art" style="left:494px;top:690px;width:60px;height:130px" role="img" aria-label="Illustration of a nurse in scrubs holding a clipboard"></div>
  <p class="abs inc-text" style="left:581px;top:736px;width:200px">Open fractures not closable at 1st surgery, those unable to adhere</p>

  <div class="abs tl-band"></div>
  <div class="abs tl-tab">Timeline</div>
  <svg class="abs" style="left:188px;top:850px" width="36" height="36" viewBox="0 0 36 36" aria-hidden="true"><circle cx="14" cy="14" r="10" fill="none" stroke="var(--navy)" stroke-width="3"/><circle cx="14" cy="12" r="3" fill="var(--coral)"/><path d="M8 19a6 5 0 0 1 12 0z" fill="var(--coral)"/><path d="M21 21l10 10" stroke="var(--navy)" stroke-width="4" stroke-linecap="round"/></svg>
  <div class="abs" style="left:243px;top:850px"><div class="tl-head">Recruitment</div><div class="tl-sub">July 2016–April 2018</div></div>
  <div class="abs divider" style="left:442px;top:841px;height:54px"></div>
  <svg class="abs" style="left:503px;top:851px" width="36" height="36" viewBox="0 0 36 36" aria-hidden="true"><circle cx="16" cy="10" r="7" fill="none" stroke="var(--navy)" stroke-width="2.5"/><path d="M4 33a12 12 0 0 1 18-11" fill="none" stroke="var(--navy)" stroke-width="2.5" stroke-linecap="round"/><path d="M28 22v11M22.5 27.5h11" stroke="var(--coral)" stroke-width="2.5" stroke-linecap="round"/></svg>
  <div class="abs" style="left:566px;top:850px"><div class="tl-head">Follow-up</div><div class="tl-sub">December 2018</div></div>

  <section class="abs fund">
    <div class="art" role="img" aria-label="Illustration of a hand holding a money bag"></div>
    <p>Funded by HRCF (project 17/204/11), supported by Brackwell Injury and Urgent Care, University of Fenmarsh, and Halden &amp; Pryce supplied dressings</p>
  </section>

  <div class="abs partner" style="left:28px;top:1028px"><span class="dot"></span>BRACKWELL INJURY &amp; URGENT CARE</div>
  <div class="abs funder" style="left:307px;top:1022px">
    <span class="mark">HRCF</span><span class="rule"></span>
    <span class="full">Health Research and<br>Care Foundation</span>
  </div>

  <div class="abs foot-strip">
    <span class="abs" style="left:28px;top:7px">Trial registration: ISRCTN48261907</span>
    <span class="abs divider" style="left:274px;top:0;height:33px"></span>
    <svg class="abs" style="left:292px;top:10px" width="13" height="13" viewBox="0 0 14 14" aria-hidden="true"><circle cx="7" cy="7" r="6" fill="none" stroke="var(--coral)" stroke-width="1.4"/><path d="M1 7h12M7 1c-3 3-3 9 0 12M7 1c3 3 3 9 0 12" fill="none" stroke="var(--coral)" stroke-width="1.1"/></svg>
    <span class="abs" style="left:314px;top:7px">plove.brantu.fenmarsh.ac.uk</span>
  </div>

  <section class="abs contact">
    <svg class="abs" style="left:27px;top:14px" width="14" height="18" viewBox="0 0 14 18" aria-hidden="true"><circle cx="7" cy="5" r="4" fill="var(--coral)"/><path d="M0 18a7 7 0 0 1 14 0z" fill="var(--coral)"/></svg>
    <div class="name">Prof. Daniel Ashford</div>
    <div class="aff">(University of Fenmarsh)</div>
    <svg class="abs" style="left:26px;top:61px" width="16" height="12" viewBox="0 0 16 12" aria-hidden="true"><rect x="1" y="1" width="14" height="10" fill="none" stroke="var(--coral)" stroke-width="1.5"/><path d="M1 1l7 6 7-6" fill="none" stroke="var(--coral)" stroke-width="1.5"/></svg>
    <div class="mail">daniel.ashford@nmsd.fenmarsh.ac.uk</div>
  </section>
</div>
</body>
</html>
```